Business Card Design with a glossy effect please

We supply and install Glass pool fencing: in Frameless, Semi Frameless, and Stainless Steel we also install Glass Balustrading, interior and exterior, plus Aluminium Tubular and Gates and Screens, and Vitra KP4482 Glass protection

Dale Purvis
M 0438516290 or T 08 9517 3364
Unit 3 / 41 Kestrel Parade, Marlow Bay 6072
ABN: 51804127739
www.tidewell-poolbarriers.com.au
info@tidewell-poolbarriers.com.au

```html
<!DOCTYPE html>
<html lang="en">
<head>
<meta charset="utf-8">
<title>Tidewell Pool Barriers – Business Card</title>
<link href="https://fonts.googleapis.com/css2?family=Roboto:wght@300;400;500&display=swap" rel="stylesheet">
<style>
  :root {
    --backdrop: #d3d4d6;
    --card: #4fc3ea;
    --card-light: #6fd0f0;
    --card-edge: #ffffff;
    --brand: #0f5b8c;
    --ink: #0b1b2a;
  }
  * { box-sizing: border-box; margin: 0; padding: 0; }
  html, body { width: 1200px; height: 900px; overflow: hidden; }
  body {
    background: radial-gradient(ellipse at center, #dcdddf 0%, var(--backdrop) 60%, #c3c4c6 100%);
    font-family: "Roboto", Arial, sans-serif;
    position: relative;
  }
  .card {
    position: absolute;
    top: 305px;
    width: 470px;
    height: 290px;
    border-radius: 24px;
    border: 2px solid var(--card-edge);
    background:
      linear-gradient(150deg, rgba(255,255,255,0.28) 0%, rgba(255,255,255,0.06) 42%, rgba(255,255,255,0) 60%),
      linear-gradient(180deg, var(--card-light), var(--card));
    box-shadow: 0 6px 14px rgba(0,0,0,0.18);
    overflow: hidden;
  }
  .card--front { left: 90px; }
  .card--back { left: 640px; }

  .brand {
    display: flex;
    align-items: center;
    gap: 14px;
    color: var(--brand);
    font-weight: 500;
  }
  .brand__mark {
    width: 34px; height: 34px;
    background: var(--brand);
    flex: none;
  }
  .card--front .brand {
    position: absolute;
    left: 50%; top: 50%;
    transform: translate(-50%, -50%);
    font-size: 30px;
    letter-spacing: 0.5px;
    white-space: nowrap;
  }
  .card--back .brand {
    position: absolute;
    left: 30px; top: 120px;
    flex-direction: column;
    align-items: flex-start;
    gap: 10px;
    font-size: 19px;
    line-height: 1.15;
    width: 150px;
  }
  .card--back .brand__mark { width: 60px; height: 60px; }

  .contact {
    position: absolute;
    left: 208px; top: 48px;
    color: var(--ink);
  }
  .contact__name { font-weight: 300; font-size: 24px; margin-bottom: 6px; }
  .contact__address { font-size: 14px; line-height: 1.25; }
  .contact__abn { font-size: 12.5px; margin-top: 6px; }
  .contact__list { list-style: none; margin-top: 26px; font-size: 10.5px; }
  .contact__list li { display: flex; align-items: flex-start; gap: 12px; margin-bottom: 10px; }
  .contact__list svg { width: 13px; height: 13px; flex: none; fill: var(--ink); }
  .contact__phones span { display: block; line-height: 1.6; }
</style>
</head>
<body>
  <section class="card card--front" aria-label="Card front">
    <div class="brand"><span class="brand__mark"></span>Tidewell Pool Barriers</div>
  </section>

  <section class="card card--back" aria-label="Card back">
    <div class="brand"><span class="brand__mark"></span>Tidewell Pool Barriers</div>
    <div class="contact">
      <p class="contact__name">Dale Purvis</p>
      <p class="contact__address">Unit 3 / 41 Kestrel Parade,<br>Marlow Bay 6072</p>
      <p class="contact__abn">ABN: 51804127739</p>
      <ul class="contact__list">
        <li>
          <svg viewBox="0 0 16 16" aria-hidden="true"><path d="M1 5c0-2 3-3 7-3s7 1 7 3v1.5h-3.5V5h-7v1.5H1z M4 8h8l2 5H2z"/></svg>
          <div class="contact__phones"><span>- 04 3851 6290</span><span>- 08 9517 3364</span></div>
        </li>
        <li>
          <svg viewBox="0 0 16 16" aria-hidden="true"><path d="M1 3h14v10H1z M2 4l6 5 6-5" stroke="#4fc3ea" stroke-width="1"/></svg>
          <span>info@tidewell-poolbarriers.com.au</span>
        </li>
        <li>
          <svg viewBox="0 0 16 16" aria-hidden="true"><circle cx="8" cy="8" r="7"/><path d="M1 8h14M8 1v14M3 4h10M3 12h10" stroke="#4fc3ea" stroke-width="0.8" fill="none"/></svg>
          <span>www.tidewell-poolbarriers.com.au</span>
        </li>
      </ul>
    </div>
  </section>
</body>
</html>
```